Global Yoga Apparel Brand Needs a Beautiful Website

We need a website design for a new Yoga brand called Vessa. We develop beautiful, stylish, sexy, comfortable yoga leggings, tops, and yoga apparel for women looking to feel their best, look their best and perform their best on and off the yoga mat.
This will go up at http://vessa.example/ (which is a landing page right now).
We would like to see simple and clean design where the focus will be on powerful images and clean background space. We will be using Shopify to start building on and here are three sites that we would love to see options based off of the look, layout and feel while making something unique at the same time:
1. Tumo.ca
2. marikoven.com
3. www.q-plume.com
The final design should look clean, beautiful, inspiring, powerful and empowering.
Target Market(s)
mostly Females 21-35 range but will be appealing to women over 35 as well.

```html
<!DOCTYPE html>
<html lang="en">
<head>
<meta charset="utf-8">
<title>Vessa — Yoga Apparel</title>
<link href="https://fonts.googleapis.com/css2?family=Roboto:wght@300;400;500;700&display=swap" rel="stylesheet">
<style>
:root{
  --ink:#111;
  --black:#000;
  --white:#fff;
  --footer-bg:#f2f2f2;
  --rule:#e2e2e2;
  --tile-bg:#5d5d60;
  --fb:#3b5998;
  --tw:#1da1f2;
  --ig:#111;
  --gp:#dd4b39;
}
*{box-sizing:border-box;margin:0;padding:0}
html,body{width:1002px;height:1200px;overflow:hidden;background:var(--white);font-family:'Roboto',sans-serif;color:var(--ink)}
.page{position:relative;width:1002px;height:1200px}
.site-header{position:absolute;left:0;top:0;width:1002px;height:71px;background:var(--black)}
.brand{position:absolute;left:83px;top:14px;color:var(--white);font-weight:700;font-size:36px;letter-spacing:-1px;line-height:1}
.header-tools{position:absolute;right:102px;top:22px;display:flex;align-items:center;gap:22px;color:var(--white)}
.cart{display:flex;align-items:center;gap:6px;font-size:22px;font-weight:400}
.hero{position:absolute;left:0;top:71px;width:1002px;height:430px;background:linear-gradient(100deg,#c7a58d 0%,#e9e2da 30%,#f4f1ec 60%,#ddd3c4 100%)}
.hero-offer{position:absolute;left:601px;top:60px;width:263px;text-align:center}
.hero-pct{font-weight:700;font-size:50px;line-height:1;letter-spacing:-1px}
.hero-pct small{font-size:15px;font-weight:400;letter-spacing:0}
.hero-rule{height:1px;background:#999;margin:14px 0 10px}
.hero-title{font-weight:300;font-size:29px;line-height:38px}
.btn-buy{display:inline-block;margin-top:14px;width:103px;height:28px;line-height:28px;background:var(--black);color:var(--white);font-weight:500;font-size:14px}
.slider-dots{position:absolute;left:454px;top:409px;display:flex;gap:4px}
.slider-dots span{width:26px;height:2px;background:#555}
.slider-dots span.active{height:3px;background:var(--black)}
.categories{position:absolute;top:515px;left:0;width:1002px;height:251px}
.category{position:absolute;top:0;width:230px;height:251px;background:linear-gradient(180deg,#6a6a6d,#5a5a5c)}
.category-label{position:absolute;left:50%;top:114px;transform:translateX(-50%);white-space:nowrap;color:var(--white);font-weight:300;font-size:26px;padding:6px 3px;border-top:1px solid var(--white);border-bottom:1px solid var(--white)}
.divider{position:absolute;left:82px;top:822px;width:838px;height:1px;background:var(--rule)}
.newsletter{position:absolute;left:0;top:870px;width:1002px;text-align:center}
.newsletter h2{font-weight:300;font-size:34px;line-height:42px}
.newsletter p{font-weight:300;font-size:18px;margin-top:8px}
.signup{position:absolute;left:267px;top:977px;width:500px;height:39px;display:flex}
.signup-input{flex:0 0 357px;border:1px solid var(--black);border-right:none;font-size:11px;padding-left:12px;display:flex;align-items:center}
.signup-btn{flex:1;background:var(--black);color:var(--white);font-weight:300;font-size:19px;display:flex;align-items:center;justify-content:center}
.site-footer{position:absolute;left:0;top:1072px;width:1002px;height:128px;background:var(--footer-bg)}
.social{position:absolute;left:408px;top:31px;display:flex;gap:13px}
.social span{width:36px;height:36px;border-radius:50%;border:1.5px solid}
.copyright{position:absolute;left:84px;top:92px;font-size:10px}
.legal{position:absolute;right:84px;top:92px;font-size:10px;display:flex}
.legal span+span{border-left:1px solid var(--ink);margin-left:14px;padding-left:14px}
</style>
</head>
<body>
<div class="page">
  <header class="site-header">
    <div class="brand">Vessa</div>
    <div class="header-tools">
      <div class="cart">
        <svg width="22" height="18" viewBox="0 0 22 18"><path d="M0 1h4l3 10h11l3-8H6" fill="none" stroke="#fff" stroke-width="2.4"/><path d="M5 3h16l-3 8H7z" fill="#fff"/><circle cx="8" cy="15.5" r="2" fill="#fff"/><circle cx="17" cy="15.5" r="2" fill="#fff"/></svg>
        <span>0</span>
      </div>
      <svg width="20" height="20" viewBox="0 0 20 20"><circle cx="8" cy="8" r="6" fill="none" stroke="#fff" stroke-width="3"/><path d="M12.5 12.5l6 6" stroke="#fff" stroke-width="3.4" stroke-linecap="round"/></svg>
      <svg width="20" height="18" viewBox="0 0 20 18"><rect y="1" width="20" height="3" fill="#fff"/><rect y="7.5" width="20" height="3" fill="#fff"/><rect y="14" width="20" height="3" fill="#fff"/></svg>
    </div>
  </header>

  <section class="hero" role="img" aria-label="Woman in a reverse plank pose on a yoga mat wearing a dark crop top and shorts, in a bright room">
    <div class="hero-offer">
      <div class="hero-pct">50%<small>off</small></div>
      <div class="hero-rule"></div>
      <div class="hero-title">Active Stretch Yoga<br>Tops &amp; Shorts</div>
      <span class="btn-buy">Buy Now</span>
    </div>
    <div class="slider-dots"><span class="active"></span><span></span><span></span></div>
  </section>

  <section class="categories">
    <div class="category" style="left:20px" role="img" aria-label="Model wearing black yoga leggings"><span class="category-label">YOGA LEGGINGS</span></div>
    <div class="category" style="left:262px" role="img" aria-label="Model wearing a blue yoga top"><span class="category-label">YOGA TOPS</span></div>
    <div class="category" style="left:508px" role="img" aria-label="Model wearing a black yoga outfit"><span class="category-label">YOGA APPAREL</span></div>
    <div class="category" style="left:751px" role="img" aria-label="Model wearing black yoga capri pants"><span class="category-label">YOGA CAPRI</span></div>
  </section>

  <div class="divider"></div>

  <section class="newsletter">
    <h2>BE THE FIRST TO KNOW</h2>
    <p>Sign up for the latest news, new releases and special promotions.</p>
  </section>
  <form class="signup">
    <div class="signup-input">Enter Your Email</div>
    <div class="signup-btn">Sign Up</div>
  </form>

  <footer class="site-footer">
    <div class="social">
      <span style="color:var(--fb)" aria-label="Social link"></span>
      <span style="color:var(--tw)" aria-label="Social link"></span>
      <span style="color:var(--ig)" aria-label="Social link"></span>
      <span style="color:var(--gp)" aria-label="Social link"></span>
    </div>
    <div class="copyright">Copyright © 2016 Vessa. All Rights Reserved.</div>
    <div class="legal"><span>Privacy Policy</span><span>Terms of Service</span><span>Return &amp; Exchange</span></div>
  </footer>
</div>
</body>
</html>
```